Website for Boutique Property Consultancy in UK

We are looking to designing a website for our Property Consultancy Services that follows a minimalistic clean style that is also bold and intriguing.
The website will be based on one landing page and a link to LinkedIn Page and email link.

Dominant features will be the company logo or icon and colours.

Brand colours provided for guidance.

Looking to achieve a minimalistic clean style that is also bold and intriguing.

"Updated"
Page 1 - Landing Page with the Hyperlinks to Pick a Service, Training Portal and Maple Nine Portal. example landing page https://tilbrook-studio.co.uk/

Page 2 - Shows all the Services and Sectors

Target Market(s)

Occupier Clients, Tech Companies, Property Developers, Infrastructure Clients and Major Consultants

Industry/Entity Type

Construction

Coding

Coded - Design and coding required

Number of Pages Required

2 page

Font styles to use
Other font styles liked:
• Century Gothic or Futuris (Headings)

Colors
0054AA
0677BA
7BADD7
CADEEF
E8F1F8
00AB8E
00BBA5
67D7C9
C6EFE9
E9F9F6

Requirements
Must have
• Company Logo, link to enquiry and LinkedIn

```html
<!DOCTYPE html>
<html lang="en">
<head>
<meta charset="utf-8">
<title>Hollin Vale — Property Consultancy</title>
<link rel="stylesheet" href="https://fonts.googleapis.com/css2?family=Questrial&display=swap">
<style>
  :root {
    --navy: #2b3050;
    --navy-deep: #2a2f4d;
    --green: #1fb86e;
    --ink: #1c1f33;
    --rule: #d3d7de;
    --card-border: #c9cde6;
    --white: #ffffff;
    --sky-1: #f6f8fb;
    --sky-2: #e7ebf0;
    --sky-3: #d9dee5;
  }
  * { box-sizing: border-box; margin: 0; padding: 0; }
  html, body { width: 1200px; height: 720px; overflow: hidden; }
  body {
    font-family: "Questrial", "Century Gothic", sans-serif;
    background: var(--white);
    color: var(--ink);
    position: relative;
  }
  .hero-backdrop {
    position: absolute; inset: 0 0 117px 0;
    background:
      linear-gradient(115deg, rgba(255,255,255,0.2) 0%, rgba(255,255,255,0.85) 45%, rgba(255,255,255,0.6) 100%),
      linear-gradient(160deg, var(--sky-1) 0%, var(--sky-2) 55%, var(--sky-3) 100%);
  }
  .page { position: relative; height: 603px; }
  .brand-name {
    position: absolute; top: 72px; left: 0; right: 0;
    text-align: center;
    font-size: 94px; line-height: 1;
    font-weight: 400;
    color: var(--navy);
    letter-spacing: 2px;
  }
  .divider {
    position: absolute; top: 193px; left: 53px; right: 59px;
    border-top: 1px solid var(--rule);
  }
  .tagline {
    position: absolute; top: 246px; left: 0; right: 0;
    text-align: center;
    font-size: 30px; letter-spacing: 2px;
    color: var(--ink);
  }
  .portal-links {
    position: absolute; top: 335px; left: 0; right: 0;
    display: flex; justify-content: center; gap: 33px;
  }
  .portal-card {
    width: 213px; height: 131px;
    background: var(--white);
    border: 1px solid var(--card-border);
    border-radius: 5px;
    box-shadow: 0 8px 18px rgba(30, 35, 60, 0.12);
    display: flex; flex-direction: column; align-items: center; justify-content: center;
    gap: 12px;
    text-decoration: none;
    color: var(--ink);
    font-size: 19px;
  }
  .portal-card svg { width: 56px; height: 52px; }
  .portal-card.is-active {
    background: var(--navy);
    border-color: var(--navy);
    color: var(--white);
  }
  .site-footer {
    position: absolute; left: 0; right: 0; bottom: 0; height: 117px;
    background: var(--navy-deep);
    display: flex; align-items: center; justify-content: center; gap: 52px;
    color: var(--white);
    font-size: 20px;
  }
  .footer-link {
    display: flex; align-items: center; gap: 10px;
    color: var(--white); text-decoration: none;
  }
  .social-mark {
    width: 30px; height: 30px; border-radius: 3px;
    background: var(--white);
    display: inline-block;
  }
</style>
</head>
<body>
  <div class="hero-backdrop" role="img" aria-label="Soft faded photograph of modern high-rise office towers seen from below"></div>

  <main class="page">
    <h1 class="brand-name">hollin vale</h1>
    <div class="divider"></div>
    <p class="tagline">Delivering Value and Redefining Boundaries</p>

    <nav class="portal-links">
      <a class="portal-card is-active" href="#services">
        <svg viewBox="0 0 56 52" fill="none" stroke="var(--green)" stroke-width="2" stroke-linejoin="round">
          <path d="M10 6 h22 l6 6 v12"/>
          <path d="M10 6 v40 h8"/>
          <path d="M20 14 h12 M20 19 h12"/>
          <rect x="18" y="28" width="30" height="19" rx="2"/>
          <path d="M27 28 v-4 h12 v4"/>
          <path d="M18 36 h30"/>
          <rect x="25" y="33" width="5" height="6"/>
          <rect x="36" y="33" width="5" height="6"/>
        </svg>
        <span>Pick a services</span>
      </a>
      <a class="portal-card" href="#training">
        <svg viewBox="0 0 56 52" fill="none" stroke="var(--green)" stroke-width="2" stroke-linejoin="round">
          <rect x="3" y="3" width="50" height="34" rx="2"/>
          <path d="M3 30 h50"/>
          <path d="M28 37 v6 M18 47 h20 M22 43 h12 v4"/>
          <circle cx="13" cy="11" r="3"/>
          <path d="M8 24 v-5 a5 5 0 0 1 10 0 l4 2 4-5"/>
          <path d="M26 10 h20 M30 15 h16 M34 20 h10"/>
        </svg>
        <span>Training Portal</span>
      </a>
      <a class="portal-card" href="#maple-nine">
        <svg viewBox="0 0 56 52" fill="none" stroke="var(--green)" stroke-width="2" stroke-linejoin="round">
          <rect x="2" y="5" width="40" height="30" rx="2"/>
          <path d="M2 29 h40"/>
          <path d="M22 35 v6 M14 46 h16 M17 41 h10 v5"/>
          <path d="M9 24 h22 M11 24 v-8 M16 24 v-12 M21 24 v-6 M26 24 v-10"/>
          <rect x="36" y="14" width="18" height="30" rx="2" fill="var(--white)"/>
          <path d="M36 20 h18"/>
          <path d="M45 26 l4 6 -4 6 -4 -6 z"/>
        </svg>
        <span>Maple Nine</span>
      </a>
    </nav>
  </main>

  <footer class="site-footer">
    <a class="footer-link" href="mailto:info@hollinvale.co.uk">
      <svg width="28" height="22" viewBox="0 0 28 22" fill="none" stroke="var(--white)" stroke-width="2" stroke-linejoin="round">
        <rect x="1.5" y="1.5" width="25" height="19" rx="3"/>
        <path d="M2 3 l12 10 12-10"/>
      </svg>
      <span>info@hollinvale.co.uk</span>
    </a>
    <a class="footer-link" href="#company-profile">
      <span class="social-mark" aria-hidden="true"></span>
      <span>hollinvale</span>
    </a>
  </footer>
</body>
</html>
```